TECH PROJECT NEEDS NEW SKINS FOR RE-BRANDING

We are a technology project that has a product (crypto wallet) nearing release, have basic designs made so far however we need NEW SKINS/ branding/ design options for this wallet to change the look and feel -- it will be called and re-branded as "NOVAK" a futuristic/ space/ edgy product so need it to look like so.

YOU ARE ALLOWED TO CHANGE + EXPERIMENT WITH THE LAYOUT/ schema and UI as you see fit -- (we are open to new and creative ideas)

(see WALLET.PNG and PROTFOLIO.PNG ATTACHED --- these are the pages we need new skins for )

(see NOVAK logo attached --- PLEASE USE THIS LOGO/ VERSIONS OF THIS LOGO IN YOUR DESIGNS/SKIN SUBMISSIONS -- WE PROVIDED THE ai file so feel free to alter the logo a bit to experiment if you want -- we are open and flexible to new creative ideas)

(FOR A MOOD BOARD FOR GUIDANCE on feel/colors/mood-- SEE "SAMPLE INTERFACE 1 & 2" ATTACHED)

Target Market(s)

TECHNOLOGY/SPACE/ FUTURE

Number of Pages Required

2 page

Colors

Designer to choose colors to be used in the design.

Requirements
Must have
• MUST USE OUR NOVAK LOGO OR A SIMILAR ALTERATION OF IT

```html
<!DOCTYPE html>
<html lang="en">
<head>
<meta charset="utf-8">
<title>NOVAK Portfolio</title>
<link rel="stylesheet" href="https://fonts.googleapis.com/css2?family=Poppins:wght@400;500;600&display=swap">
<style>
:root{
  --page:#ffffff;
  --sidebar:#0e1730;
  --header:#080d1c;
  --main:#111731;
  --main-glow:#0f4a7a;
  --active:#18308f;
  --accent:#1a6bff;
  --label:#2f6bff;
  --card:#17245a;
  --text:#ffffff;
  --muted:#9aa3c0;
  --line:#2a3350;
  --green:#3ddc4a;
  --yellow:#f5d90a;
  --red:#e8141e;
  --orange:#f57c14;
  --cyan:#19c3f0;
  --magenta:#c41ce8;
  --amber:#f5a914;
  --link:#1aa7ff;
}
*{box-sizing:border-box;margin:0;padding:0}
html,body{width:1200px;height:1200px;overflow:hidden;background:var(--page);font-family:"Poppins",sans-serif;color:var(--text)}
.stage{position:absolute;left:0;top:204px;width:1500px;height:990px;transform:scale(.8);transform-origin:0 0;overflow:hidden;
  background:radial-gradient(ellipse 900px 500px at 1150px 1000px,var(--main-glow),transparent 70%),var(--main)}
.abs{position:absolute}
.sidebar{left:0;top:0;width:160px;height:990px;background:linear-gradient(180deg,#0d1935,#0b1328)}
.brand{left:30px;top:44px;display:flex;align-items:center;gap:8px;font-size:22px;font-weight:500;letter-spacing:3px}
.brand i{width:16px;height:16px;border:2px solid var(--text);border-radius:3px;display:block}
.nav-active{left:53px;top:262px;width:107px;height:63px;background:var(--active);border-radius:32px 0 0 32px}
.nav-icon{left:84px;width:36px;height:36px}
.settings{left:48px;top:830px;width:62px;text-align:center;color:var(--muted);font-size:15px}
.settings svg{display:block;margin:0 auto 8px}
.header{left:160px;top:0;width:1340px;height:112px;background:var(--header)}
.avatar{left:232px;top:17px;width:70px;height:80px;clip-path:polygon(50% 0,100% 25%,100% 75%,50% 100%,0 75%,0 25%);background:linear-gradient(160deg,#d9d4cf,#7c6a5e)}
.user-name{left:325px;top:36px;font-size:17px;font-weight:500}
.user-handle{left:323px;top:63px;font-size:13px;color:#3a4260}
.field{top:36px;font-size:17px;border-bottom:1px solid var(--line);height:39px}
.search{left:464px;width:373px;padding-left:4px}
.filter{left:876px;width:298px;padding-left:5px}
.add-btn{left:1257px;top:34px;width:211px;height:45px;border:2px solid #1e50c8;border-radius:23px;box-shadow:0 0 14px rgba(30,90,255,.5);font-size:15px;font-weight:600;display:flex;align-items:center;justify-content:center}
.map{left:980px;top:112px;width:390px;height:180px;opacity:.25;background:radial-gradient(ellipse at 50% 40%,#5a6488,transparent 70%)}
.title{left:232px;top:158px;font-size:23px;font-weight:600}
.tabs{left:232px;top:232px;display:flex;font-size:13px;font-weight:600}
.tabs span{margin-right:52px}
.tab-on{position:absolute;left:66px;top:-7px;width:68px;height:31px;border:2px solid #1e50c8;border-radius:16px;color:var(--yellow);display:flex;align-items:center;justify-content:center}
.action{left:1356px;top:167px;width:111px;height:30px;border:1px solid #2b4aa0;border-radius:3px;font-size:13px;display:flex;align-items:center;padding-left:9px;gap:10px}
.action b{width:12px;height:12px;border:1px solid var(--text)}
.ring{top:300px;width:130px;height:130px}
.ring-value{position:absolute;left:0;top:69px;width:130px;text-align:center;font-size:12px;font-weight:500}
.ring-dot{position:absolute;left:57px;top:45px;width:16px;height:16px;border-radius:50%;background:var(--text)}
.est{left:1282px;top:317px}
.est .label{color:var(--label);font-size:15px}
.est .amount{font-size:30px;margin-top:6px}
.est .count{font-size:22px;margin-top:2px}
.card{top:478px;width:193px;height:68px;background:var(--card);border-radius:3px;padding:10px 10px}
.card .label{font-size:12px;color:var(--label)}
.card .amount{font-size:18px;margin-top:2px}
.card .pct{position:absolute;right:11px;top:40px;font-size:11px}
.card .up{position:absolute;right:20px;top:18px}
.table{left:232px;top:592px;width:1236px;border-collapse:collapse;font-size:14px}
.table th{height:51px;font-weight:400;color:var(--muted);font-size:14px;border-top:1px solid var(--line)}
.table th:last-child{border-right:1px solid var(--line)}
.table th.on{background:#0a5cff;color:var(--text);font-weight:500;width:134px}
.table td{height:51px;text-align:center;font-weight:600;border-top:1px solid var(--line)}
.table tr:last-child td{border-bottom:1px solid var(--line)}
.table td:last-child{border-right:1px solid var(--line)}
.table td.asset{text-align:left;padding-left:32px;white-space:nowrap}
.asset i{display:inline-block;width:14px;height:14px;border-radius:50%;margin-right:12px;vertical-align:-2px}
.chg{display:inline-flex;align-items:center;gap:7px}
.chg svg{display:block}
.amber{color:var(--amber)} .pos{color:var(--green)}
.link{color:var(--link);font-size:12px}
</style>
</head>
<body>
<div class="stage">
  <aside class="abs sidebar">
    <div class="abs brand"><i></i>NOVAK</div>
    <div class="abs nav-active"></div>
    <svg class="abs nav-icon" style="top:189px" viewBox="0 0 36 36" fill="none" stroke="#8c96b5" stroke-width="1.6"><rect x="2" y="2" width="32" height="32"/><line x1="2" y1="10" x2="34" y2="10"/><rect x="6" y="15" width="10" height="8"/><rect x="6" y="26" width="10" height="5"/><line x1="20" y1="17" x2="30" y2="17"/><line x1="20" y1="28" x2="30" y2="28"/></svg>
    <svg class="abs nav-icon" style="top:275px" viewBox="0 0 36 36" fill="none" stroke="#c5cde6" stroke-width="1.6"><rect x="4" y="2" width="22" height="30"/><rect x="8" y="7" width="5" height="5"/><line x1="16" y1="9" x2="22" y2="9"/><rect x="8" y="16" width="5" height="5"/><line x1="16" y1="18" x2="22" y2="18"/><line x1="8" y1="26" x2="22" y2="26"/><circle cx="30" cy="30" r="5" fill="#1a6bff" stroke="none"/></svg>
    <svg class="abs nav-icon" style="top:363px" viewBox="0 0 36 36" fill="none" stroke="#8c96b5" stroke-width="1.6"><rect x="2" y="10" width="30" height="22" rx="3"/><path d="M5 10 L26 4 L28 10"/><rect x="24" y="18" width="8" height="6"/></svg>
    <svg class="abs nav-icon" style="top:449px" viewBox="0 0 36 36" fill="none" stroke="#8c96b5" stroke-width="1.6"><path d="M22 2 L8 20 H18 L12 34 L28 14 H18 Z"/></svg>
    <svg class="abs nav-icon" style="top:533px" viewBox="0 0 36 36" fill="none" stroke="#8c96b5" stroke-width="1.6"><path d="M8 28 H28 A6 6 0 0 0 27 16 A9 9 0 0 0 10 16 A6 6 0 0 0 8 28 Z"/></svg>
    <div class="abs settings">
      <svg width="34" height="34" viewBox="0 0 34 34" fill="none" stroke="#6f7899" stroke-width="1.6"><circle cx="17" cy="17" r="5"/><path d="M17 3 L20 7 L25 6 L26 11 L31 14 L28 17 L31 20 L26 23 L25 28 L20 27 L17 31 L14 27 L9 28 L8 23 L3 20 L6 17 L3 14 L8 11 L9 6 L14 7 Z"/></svg>
      Settings
    </div>
  </aside>

  <header class="abs header"></header>
  <div class="abs avatar" role="img" aria-label="User profile photo"></div>
  <div class="abs user-name">Arin K</div>
  <div class="abs user-handle">arin.kv</div>
  <div class="abs field search">Search
    <svg class="abs" style="left:344px;top:-2px" width="30" height="30" viewBox="0 0 30 30" fill="none" stroke="#c5cde6" stroke-width="1.6"><circle cx="12" cy="12" r="10"/><line x1="19" y1="19" x2="28" y2="28"/></svg>
  </div>
  <div class="abs field filter">ALL
    <svg class="abs" style="left:284px;top:-2px" width="14" height="24" viewBox="0 0 14 24" fill="none" stroke="#c5cde6" stroke-width="1.8"><path d="M2 9 L7 4 L12 9 M2 15 L7 20 L12 15"/></svg>
  </div>
  <div class="abs add-btn">+ ADD TRANSACTIONS</div>

  <div class="abs map" role="img" aria-label="Faint dotted world map decoration"></div>
  <h1 class="abs title">PROTFOLIO</h1>
  <div class="abs tabs"><span>ALL</span><span style="margin-left:100px">WEEK</span><span>MONTH</span><span>YEAR</span><div class="tab-on">24 H</div></div>
  <div class="abs action"><b></b>Action
    <svg width="14" height="8" viewBox="0 0 14 8" fill="none" stroke="#fff" stroke-width="1.5"><path d="M1 1 L7 7 L13 1"/></svg>
  </div>

  <div class="abs ring" style="left:231px"><svg width="130" height="130" viewBox="0 0 130 130"><circle cx="65" cy="65" r="61" fill="none" stroke="#6e7592" stroke-width="4"/><circle cx="65" cy="65" r="61" fill="none" stroke="var(--green)" stroke-width="5" stroke-dasharray="268 400" transform="rotate(-30 65 65)"/><circle cx="65" cy="65" r="46" fill="#121a38" stroke="#6e7592" stroke-width="2"/></svg><span class="ring-dot"></span><div class="ring-value">$61,045.78</div></div>
  <div class="abs ring" style="left:398px"><svg width="130" height="130" viewBox="0 0 130 130"><circle cx="65" cy="65" r="61" fill="none" stroke="#6e7592" stroke-width="4"/><circle cx="65" cy="65" r="61" fill="none" stroke="var(--yellow)" stroke-width="5" stroke-dasharray="170 400" transform="rotate(10 65 65)"/><circle cx="65" cy="65" r="46" fill="#121a38" stroke="#6e7592" stroke-width="2"/></svg><span class="ring-dot"></span><div class="ring-value">$$9,200.50</div></div>
  <div class="abs ring" style="left:565px"><svg width="130" height="130" viewBox="0 0 130 130"><circle cx="65" cy="65" r="61" fill="none" stroke="#6e7592" stroke-width="4"/><circle cx="65" cy="65" r="61" fill="none" stroke="var(--red)" stroke-width="5" stroke-dasharray="200 400" transform="rotate(-10 65 65)"/><circle cx="65" cy="65" r="46" fill="#121a38" stroke="#6e7592" stroke-width="2"/></svg><span class="ring-dot"></span><div class="ring-value">$$14,800.12</div></div>
  <div class="abs ring" style="left:732px"><svg width="130" height="130" viewBox="0 0 130 130"><circle cx="65" cy="65" r="61" fill="none" stroke="#6e7592" stroke-width="4"/><circle cx="65" cy="65" r="61" fill="none" stroke="var(--orange)" stroke-width="5" stroke-dasharray="190 400" transform="rotate(0 65 65)"/><circle cx="65" cy="65" r="46" fill="#121a38" stroke="#6e7592" stroke-width="2"/></svg><span class="ring-dot"></span><div class="ring-value">$12,800.12</div></div>
  <div class="abs ring" style="left:898px"><svg width="130" height="130" viewBox="0 0 130 130"><circle cx="65" cy="65" r="61" fill="none" stroke="#6e7592" stroke-width="4"/><circle cx="65" cy="65" r="61" fill="none" stroke="var(--cyan)" stroke-width="5" stroke-dasharray="200 400" transform="rotate(5 65 65)"/><circle cx="65" cy="65" r="46" fill="#121a38" stroke="#6e7592" stroke-width="2"/></svg><span class="ring-dot"></span><div class="ring-value">$15,800.12</div></div>
  <div class="abs ring" style="left:1065px"><svg width="130" height="130" viewBox="0 0 130 130"><circle cx="65" cy="65" r="61" fill="none" stroke="#6e7592" stroke-width="4"/><circle cx="65" cy="65" r="61" fill="none" stroke="var(--magenta)" stroke-width="5" stroke-dasharray="200 400" transform="rotate(5 65 65)"/><circle cx="65" cy="65" r="46" fill="#121a38" stroke="#6e7592" stroke-width="2"/></svg><span class="ring-dot"></span><div class="ring-value">$13,800.12</div></div>

  <div class="abs est"><div class="label">Est. Assets Value</div><div class="amount">$ 1,270,000.98</div><div class="count">6 Assets</div></div>

  <div class="abs card" style="left:232px"><div class="label">Portfolio Change</div><div class="amount">$ 1.234.100,89</div><svg class="up" width="16" height="16" viewBox="0 0 16 16"><circle cx="8" cy="8" r="8" fill="#fff"/><path d="M4.5 9.5 L8 6 L11.5 9.5" fill="none" stroke="#17245a" stroke-width="2"/></svg><span class="pct">36,9%</span></div>
  <div class="abs card" style="left:441px"><div class="label">Profit/Loss</div><div class="amount">$ 1.234.100,89</div><svg class="up" width="16" height="16" viewBox="0 0 16 16"><circle cx="8" cy="8" r="8" fill="#fff"/><path d="M4.5 9.5 L8 6 L11.5 9.5" fill="none" stroke="#17245a" stroke-width="2"/></svg><span class="pct">36,9%</span></div>
  <div class="abs card" style="left:650px"><div class="label">14H Profit/Loss</div><div class="amount">$ 1.234.100,89</div><svg class="up" width="16" height="16" viewBox="0 0 16 16"><circle cx="8" cy="8" r="8" fill="#fff"/><path d="M4.5 9.5 L8 6 L11.5 9.5" fill="none" stroke="#17245a" stroke-width="2"/></svg><span class="pct">36,9%</span></div>
  <div class="abs card" style="left:859px"><div class="label">Best Assets</div><div class="amount">Vortex-VTX</div><svg class="up" width="16" height="16" viewBox="0 0 16 16"><circle cx="8" cy="8" r="8" fill="#fff"/><path d="M4.5 9.5 L8 6 L11.5 9.5" fill="none" stroke="#17245a" stroke-width="2"/></svg><span class="pct">36,9%</span></div>
  <div class="abs card" style="left:1068px"><div class="label">Worst Assets</div><div class="amount">Solarion - SLR</div><svg class="up" width="16" height="16" viewBox="0 0 16 16"><circle cx="8" cy="8" r="8" fill="var(--amber)"/><path d="M4.5 6.5 L8 10 L11.5 6.5" fill="none" stroke="#17245a" stroke-width="2"/></svg><span class="pct amber">46,5%</span></div>
  <div class="abs card" style="left:1277px"><div class="label">Portfolio Change</div><div class="amount">$ 1.234.100,89</div><svg class="up" width="16" height="16" viewBox="0 0 16 16"><circle cx="8" cy="8" r="8" fill="#fff"/><path d="M4.5 9.5 L8 6 L11.5 9.5" fill="none" stroke="#17245a" stroke-width="2"/></svg><span class="pct">36,9%</span></div>

  <table class="abs table">
    <thead><tr><th class="on">ASSET NAME</th><th>MARKET CAP</th><th>VOLUME 24H</th><th>% CHANGE</th><th>LAST PRICE</th><th>BALANCE</th><th>VALUE</th><th>PORTFOLIO</th><th>ACTIONS</th></tr></thead>
    <tbody>
      <tr><td class="asset" style="box-shadow:inset 2px 0 var(--green)"><i style="background:var(--green)"></i>Solarion - SLR</td><td>120 B</td><td>2,7 B</td><td><span class="chg amber"><svg width="17" height="17" viewBox="0 0 16 16"><circle cx="8" cy="8" r="8" fill="var(--amber)"/><path d="M4.5 6.5 L8 10 L11.5 6.5" fill="none" stroke="#111731" stroke-width="2"/></svg>46,5%</span></td><td>$ 3,664.99</td><td>10.00002142 SLR</td><td>$36,649.98</td><td>12,7 %</td><td class="link">SEND - ERCVIED</td></tr>
      <tr><td class="asset" style="box-shadow:inset 2px 0 var(--yellow)"><i style="background:var(--yellow)"></i>Quasar - QSR</td><td>30 B</td><td>2,7 B</td><td><span class="chg amber"><svg width="17" height="17" viewBox="0 0 16 16"><circle cx="8" cy="8" r="8" fill="var(--amber)"/><path d="M4.5 6.5 L8 10 L11.5 6.5" fill="none" stroke="#111731" stroke-width="2"/></svg>22,6%</span></td><td>$ 3,664.99</td><td>10.00002142 QSR</td><td>$36,649.98</td><td>12,7 %</td><td class="link">SEND - ERCVIED</td></tr>
      <tr><td class="asset" style="box-shadow:inset 2px 0 var(--red)"><i style="background:var(--red)"></i>Nebula - NBL</td><td>30 B</td><td>2,7 B</td><td><span class="chg amber"><svg width="17" height="17" viewBox="0 0 16 16"><circle cx="8" cy="8" r="8" fill="var(--amber)"/><path d="M4.5 6.5 L8 10 L11.5 6.5" fill="none" stroke="#111731" stroke-width="2"/></svg>18,25</span></td><td>$ 3,664.99</td><td>10.00002142 NBL</td><td>$36,649.98</td><td>12,7 %</td><td class="link">SEND - ERCVIED</td></tr>
      <tr><td class="asset" style="box-shadow:inset 2px 0 var(--orange)"><i style="background:var(--orange)"></i>Comet - CMT</td><td>30 B</td><td>2,7 B</td><td><span class="chg amber"><svg width="17" height="17" viewBox="0 0 16 16"><circle cx="8" cy="8" r="8" fill="var(--amber)"/><path d="M4.5 6.5 L8 10 L11.5 6.5" fill="none" stroke="#111731" stroke-width="2"/></svg>10,9%</span></td><td>$ 3,664.99</td><td>10.00002142 CMT</td><td>$36,649.98</td><td>12,7 %</td><td class="link">SEND - ERCVIED</td></tr>
      <tr><td class="asset" style="box-shadow:inset 2px 0 var(--cyan)"><i style="background:var(--cyan)"></i>Pulsar - PLS</td><td>30 B</td><td>2,7 B</td><td><span class="chg amber"><svg width="17" height="17" viewBox="0 0 16 16"><circle cx="8" cy="8" r="8" fill="var(--amber)"/><path d="M4.5 6.5 L8 10 L11.5 6.5" fill="none" stroke="#111731" stroke-width="2"/></svg>10,9%</span></td><td>$ 3,664.99</td><td>10.00002142 PLS</td><td>$36,649.98</td><td>12,7 %</td><td class="link">SEND - ERCVIED</td></tr>
      <tr><td class="asset" style="box-shadow:inset 2px 0 var(--magenta)"><i style="background:var(--magenta)"></i>Vortex - VTX</td><td>30 B</td><td>2,7 B</td><td><span class="chg pos"><svg width="17" height="17" viewBox="0 0 16 16"><circle cx="8" cy="8" r="8" fill="var(--green)"/><path d="M4.5 9.5 L8 6 L11.5 9.5" fill="none" stroke="#111731" stroke-width="2"/></svg>36,9%</span></td><td>$ 3,664.99</td><td>10.00002142 VTX</td><td>$36,649.98</td><td>12,7 %</td><td class="link">SEND - ERCVIED</td></tr>
    </tbody>
  </table>
</div>
</body>
</html>
```